Packaging label for a electronic guitar pickup company

Hi!
We are Velvet Anchor, LLC and we make electronic guitar pickups, guitars and other musical products.
What we need is rocking label for our packaging denoting our company name and product name.
Here are some needed:
1. Name and logo
2. The words 'exact replica of TRK Bellwinder pickups'
3. Made in the USA
4. Product name: Copper Tide 1969 (there are four different names in this product category)
5. website info: www. velvet-anchor.example
This of the 1960's for inspiration for the label. Think Rory Caldwell and the music and vibe that he represented.
The box will be no bigger than a 4"x6", so whatever is created, needs to be able to be printed on this surface or smaller (most likely a little bit smaller size)
Please note that the winged logo does not need to be pink...
Okay, have fun...
Target Market(s)
Guitar players who are seeking the authentic sound of 60"s pickups and the sound that came from Bellwinders of that era...
People who love the sound of Rory Caldwell playing a guitar
Industry/Entity Type
Electronic
Look and feel
Each slider illustrates characteristics of the customer's brand and the style your logo design should communicate.

```html
<!DOCTYPE html>
<html lang="en">
<head>
<meta charset="utf-8">
<title>Velvet Anchor — Copper Tide 1969 Pickup Label</title>
<link rel="stylesheet" href="https://fonts.googleapis.com/css2?family=Lobster+Two:ital,wght@1,700&display=swap">
<style>
  :root {
    --backdrop: #7d5e33;
    --label-cream: #fdf1da;
    --band-orange: #d9781c;
    --band-brown: #5a2410;
    --panel-light: #fcebc4;
    --panel-warm: #f2c27a;
    --ink: #4a1808;
    --medallion: #6e3018;
    --medallion-text: #fbe6bb;
  }
  html, body {
    margin: 0;
    padding: 0;
    width: 1200px;
    height: 1000px;
    overflow: hidden;
    background: var(--backdrop);
  }
  .canvas {
    display: block;
    width: 1200px;
    height: 1000px;
  }
  .label-text {
    font-family: "Lobster Two", cursive;
    font-style: italic;
    font-weight: 700;
    fill: var(--ink);
  }
  .product-name { font-size: 46px; letter-spacing: 4px; }
  .brand-name { font-size: 48px; fill: var(--medallion-text); }
  .claim { font-size: 33px; letter-spacing: 1px; }
  .origin { font-size: 19px; }
</style>
</head>
<body>
<svg class="canvas" viewBox="0 0 1200 1000" xmlns="http://www.w3.org/2000/svg">
  <defs>
    <linearGradient id="panelFill" x1="0" y1="0" x2="0.3" y2="1">
      <stop offset="0" stop-color="var(--panel-light)"/>
      <stop offset="0.55" stop-color="var(--panel-warm)"/>
      <stop offset="1" stop-color="var(--panel-light)"/>
    </linearGradient>
    <filter id="labelShadow" x="-10%" y="-10%" width="120%" height="120%">
      <feDropShadow dx="0" dy="4" stdDeviation="6" flood-color="#2e1f0c" flood-opacity="0.45"/>
    </filter>
    <path id="productArc" d="M372,440 A180,180 0 0 1 732,440"/>
  </defs>

  <g class="label">
    <path class="label-border" filter="url(#labelShadow)" fill="var(--label-cream)"
      d="M310,820 V385 A260,260 0 0 1 830,385 V820 Q830,840 810,840 H330 Q310,840 310,820 Z"/>
    <path class="label-band-orange" fill="var(--band-orange)"
      d="M330,805 V385 A240,240 0 0 1 810,385 V805 Q810,822 793,822 H347 Q330,822 330,805 Z"/>
    <path class="label-band-brown" fill="var(--band-brown)"
      d="M343,795 V385 A227,227 0 0 1 797,385 V795 Q797,810 782,810 H358 Q343,810 343,795 Z"/>
    <path class="label-panel" fill="url(#panelFill)"
      d="M356,786 V385 A214,214 0 0 1 784,385 V786 Q784,798 772,798 H368 Q356,798 356,786 Z"/>

    <circle class="brand-circle" cx="530" cy="415" r="120" fill="var(--medallion)"/>
    <text class="label-text brand-name" text-anchor="middle">
      <tspan x="530" y="410">Velvet</tspan>
      <tspan x="530" y="464">Anchor</tspan>
    </text>

    <text class="label-text product-name">
      <textPath href="#productArc" startOffset="50%" text-anchor="middle">Copper Tide 1969</textPath>
    </text>

    <text class="label-text claim" x="553" y="598" text-anchor="middle">Exact Replica</text>
    <text class="label-text claim" x="553" y="645" text-anchor="middle">of</text>
    <text class="label-text claim" x="558" y="692" text-anchor="middle">TRK Bellwinder Pickups</text>

    <text class="label-text origin" x="560" y="781" text-anchor="middle">Made in USA</text>
  </g>
</svg>
</body>
</html>
```